Rinsely Surface Cleaning - Business Card Design

Use company logo and design a new business card. We are looking for a front and back design. The back should be a dark purple background. We want the back to show cartoon-like soap bubbles chasing mildew cartoon shaped figures. This gives the idea that Rinsely Surface Cleaning provides exterior washing services that work. No mildew stands a chance when Rinsely Surface Cleaning shows up to work. The mildew cartoon images should be green in color, have eyes, and look scared of the bubbles. The bubbles should be light blue in color and have eyes that looked excited to be there.
We will advertise on Chatterly and Pixalonia. These Chatterly and Pixalonia icons should be somewhere on the card.

```html
<!DOCTYPE html>
<html lang="en">
<head>
<meta charset="utf-8">
<title>Rinsely Surface Cleaning – Business Card</title>
<link rel="stylesheet" href="https://fonts.googleapis.com/css2?family=Roboto:wght@400;500;700&display=swap">
<style>
  :root {
    --stage: #353535;
    --purple: #3b2260;
    --blue: #4a66b0;
    --white: #ffffff;
    --paper: #f4f4f4;
    --paper-shade: #e6e6e6;
  }
  * { margin: 0; padding: 0; box-sizing: border-box; }
  html, body {
    width: 1075px; height: 1200px; overflow: hidden;
    background: var(--stage);
    font-family: "Roboto", Arial, sans-serif;
  }
  .canvas { position: relative; width: 1075px; height: 1200px; }

  .card {
    position: absolute;
    width: 664px; height: 395px;
    overflow: hidden;
  }
  .card-front { left: 206px; top: 187px; background: var(--purple); }
  .card-back {
    left: 203px; top: 637px;
    background: linear-gradient(120deg, var(--paper-shade) 0%, var(--paper) 45%, var(--white) 100%);
  }

  .front-art { position: absolute; left: 0; top: 0; width: 664px; height: 395px; }

  .contact-block {
    position: absolute; inset: 0;
    text-align: right; color: var(--white);
  }
  .person-name {
    position: absolute; right: 42px; top: 93px;
    font-weight: 700; font-size: 24px; line-height: 28px; white-space: nowrap;
  }
  .person-title {
    position: absolute; right: 47px; top: 121px;
    font-weight: 400; font-size: 19px; line-height: 24px; white-space: nowrap;
  }
  .address {
    position: absolute; right: 42px; top: 178px;
    font-style: normal; font-size: 19px; line-height: 23.5px; white-space: nowrap;
  }
  .contact-list {
    position: absolute; right: 46px; top: 285px;
    list-style: none; font-size: 19px; line-height: 23.5px;
  }
  .contact-list li { display: flex; justify-content: flex-end; align-items: center; gap: 7px; white-space: nowrap; }
  .contact-list svg { width: 17px; height: 17px; flex: none; }

  .back-decor { position: absolute; left: 0; top: 0; width: 664px; height: 395px; }

  .brand {
    position: absolute; left: 160px; top: 0; width: 400px; height: 395px;
    color: var(--purple); font-weight: 700;
  }
  .brand-main { position: absolute; left: 0; top: 126px; font-size: 100px; line-height: 100px; letter-spacing: -2px; white-space: nowrap; }
  .brand-sub { position: absolute; left: 4px; top: 248px; font-size: 21px; line-height: 26px; letter-spacing: 0.5px; white-space: nowrap; }
</style>
</head>
<body>
<main class="canvas">

  <section class="card card-front" aria-label="Business card front">
    <svg class="front-art" viewBox="0 0 664 395" role="img" aria-label="Illustration of a pressure washer spraying soap bubbles over a globe">
      <polygon points="0,0 262,0 130,170 110,395 0,395" fill="var(--blue)"/>
    </svg>

    <div class="contact-block">
      <h1 class="person-name">MARCUS DELANEY</h1>
      <p class="person-title">Managing Director</p>
      <address class="address">
        88, Harbor Mill Road<br>Eastbrook<br>30418, Northland
      </address>
      <ul class="contact-list">
        <li>055-318 204 617
          <svg viewBox="0 0 16 16" aria-hidden="true"><path d="M4 2 L6.5 5 L5 6.8 C6 9 7 10 9.2 11 L11 9.5 L14 12 L12.5 14 C7 14 2 9 2 3.5 Z" fill="none" stroke="#fff" stroke-width="1.6" stroke-linejoin="round"/></svg>
        </li>
        <li>hello@rinsely.co
          <svg viewBox="0 0 16 16" aria-hidden="true"><rect x="1" y="3.5" width="14" height="9.5" fill="#fff"/><path d="M1.5 4 L8 9 L14.5 4" fill="none" stroke="var(--purple)" stroke-width="1.2"/></svg>
        </li>
        <li>www.rinselyclean.co
          <svg viewBox="0 0 16 16" aria-hidden="true"><g fill="none" stroke="#fff" stroke-width="1.3"><circle cx="8" cy="8" r="6.5"/><ellipse cx="8" cy="8" rx="3" ry="6.5"/><line x1="1.5" y1="8" x2="14.5" y2="8"/><line x1="2.5" y1="5" x2="13.5" y2="5"/><line x1="2.5" y1="11" x2="13.5" y2="11"/></g></svg>
        </li>
      </ul>
    </div>
  </section>

  <section class="card card-back" aria-label="Business card back">
    <svg class="back-decor" viewBox="0 0 664 395" role="img" aria-label="Faint embossed pressure washer and globe illustration">
      <defs>
        <radialGradient id="emboss" cx="0.28" cy="0.7" r="0.45">
          <stop offset="0" stop-color="#ffffff" stop-opacity="0.55"/>
          <stop offset="1" stop-color="#ffffff" stop-opacity="0"/>
        </radialGradient>
      </defs>
      <rect x="0" y="0" width="664" height="395" fill="url(#emboss)"/>
    </svg>

    <div class="brand">
      <span class="brand-main">Rinsely</span>
      <span class="brand-sub">SURFACE CLEANING</span>
    </div>
  </section>

</main>
</body>
</html>
```